Business Card and Letterhead for Copperfield Reed - (Have Logo)

Update 4: Removed company reg no from business card details as it looked a bit out of place. Updated services list.
UPDATE 3
Sorry, I got the address a little bit wrong, have updated it below. Sorry for any inconvenience caused.
UPDATE 2
Finally I have the details for the business cards and letterhead. Submissions already made do not have to be updated unless shortlisted, if all new submissions could include the details for me, Simon, that would be very much appreciated and help with the final shortlist selection. I intend to share a shortlist of the three best entries with past and existing customers for their feedback and opinions. Thank you all again for your time.
Here are the details.
Simon Latchford
Web Developer
T: 01632 418 720
E: simon@copperfieldreed.example
www.copperfieldreed.example
Professional Photography
Web Solutions & E-Commerce
Audio & HD Video Production
Marketing & Promotions
Identity and Branding
Copperfield Reed Ltd
Suite 20938, 3rd Floor
212-224 Marlowe Row
London, EC2R 8KT
Company Reg. No: 09264183
The order and the layout of the information are of course down to the design, but the company registration number should be smaller and less prominent. The formatting of the telephone and email address using a T: and an E: I am not sure about and again if it is Tel: or Email: or Icons is up to the design.
The Company No. on the letterhead should read (somewhere in small text along the bottom):
Copperfield Reed is a Ltd Company registered in England & Wales, Registration No. 09264183.
The second business card details are
Martin Oakley
Photographer
T: 01632 418 720
E: martin@copperfieldreed.example
Everything else the same of course.
Thank you again for all the submissions so far.
END OF UPDATE 2
-
UPDATE 1: Please do not alter the logo nor the logo colours. (This was a previous pixel bazaar project and I am extremely happy with it. The icon can stand alone of course, but I have had to eliminate all entries that have made it black and white, or reversed the icon.) I would like to thank everyone that has participated so far and am very grateful for all your thought and time.
End of Update 1
-
Original Brief:
I have attached the logo vector file.
Following a superb logo from a previous Pixel Bazaar project I am now looking for a business card design and (although less important) a letterhead as well.
I must admit I tried to do it myself but could only come up with the usual amateur stuff that in comparison to the quality of the logo looked awful.
About Us
Copperfield Reed Ltd will be a new company due to start in January. It is really just me (a web developer) and my friend (a photographer). We will be aiming at the usual small to medium sized businesses in the local area, selling various digital services including photographic services to the public, web hosting and development, commercial photography, modelling services (not us!), full video and film production and possibly a bit of marketing as well. (Really it is anything we can do professionally all lumped together! We met running seperate businesses which have both since closed)
We will not be competing on price. We plan to be expensive but fair. Certainly not the cheapest.
What we are looking for
Business Card
I imagine a double sided business card, which will be used for more than one person. I imagine the front to be the same for everyone and the persons details to be on the back, although this is of course only my thoughts and I am of course completely open to any ideas.
The card could also have a services list or a bit about what we do on it. It might feature the website address, our business address (mail forwarding address) or our registered company number.
Or it might have none of that, we are completely open to any ideas and have no real fixed opinions. I just want it to be really nice :-)
Letterhead (secondary importance)
We will make our decision primarily on the business card, although a mathcing letterhead would be fantastic. Something standardish in format and simple, although again, all ideas are welcomed.
I hope that is enough information but if you have any questions I will answer them as fully and as quickly as possible.
Thank you once again and I really look forward to seeing your ideas and picking a winner.
Simon L.
Small businesses AND the general public
Film Production

```html
<!DOCTYPE html>
<html lang="en">
<head>
<meta charset="utf-8">
<title>Copperfield Reed – Business Cards</title>
<link rel="stylesheet" href="https://fonts.googleapis.com/css2?family=Arimo:ital,wght@0,400;0,700;1,700&family=Roboto+Condensed:wght@700&display=swap">
<style>
  :root {
    --page: #ffffff;
    --board: #ffffff;
    --card: #000000;
    --ink: #ffffff;
    --brand-red: #b5121b;
    --rule-red: #8e1016;
    --muted: #454545;
  }
  * { margin: 0; padding: 0; box-sizing: border-box; }
  html, body { width: 1200px; height: 900px; overflow: hidden; background: var(--page); }
  .canvas { position: relative; width: 1200px; height: 900px; }
  .board {
    position: absolute; left: 20px; top: 20px; width: 1138px; height: 840px;
    background: var(--board); border-radius: 90px;
    box-shadow: 4px 6px 14px rgba(0,0,0,0.35);
  }
  .card {
    position: absolute; top: 66px; width: 524px; height: 746px;
    background: var(--card); color: var(--ink); overflow: hidden;
  }
  .card--simon { left: 59px; }
  .card--martin { left: 595px; }
  .card .rules { position: absolute; inset: 0; }
  .details { position: absolute; top: 0; width: 300px; }
  .card--simon .details { left: 119px; }
  .card--martin .details { left: 235px; }
  .services { position: absolute; top: 143px; list-style: none;
    font-family: "Roboto Condensed", "Arial Narrow", sans-serif; font-weight: 700;
    font-size: 12.5px; letter-spacing: 0.2px; }
  .services li { height: 28.5px; line-height: 16px; white-space: nowrap; }
  .phone { position: absolute; top: 310px; font-family: Arimo, Arial, sans-serif; font-size: 17px; white-space: nowrap; }
  .email, .reg, .web { position: absolute; font-family: "Roboto Condensed", "Arial Narrow", sans-serif;
    font-weight: 700; font-size: 12.5px; white-space: nowrap; }
  .email { top: 352px; }
  .person { position: absolute; top: 431px; font-family: Arimo, Arial, sans-serif; font-weight: 700;
    font-size: 16px; line-height: 21px; white-space: nowrap; }
  .person .name { color: var(--brand-red); }
  .person .name em { font-style: italic; }
  .person .role { color: var(--muted); }
  .reg { top: 515px; }
  .address { position: absolute; top: 554px; font-family: Arimo, Arial, sans-serif; font-size: 17px;
    line-height: 21px; font-style: normal; white-space: nowrap; }
  .address .city { display: block; margin-top: 21px; }
  .web { top: 681px; }
  .wordmark {
    position: absolute; top: 420px; width: 90px;
    font-family: "Roboto Condensed", "Arial Narrow", sans-serif; font-weight: 700;
    font-size: 15px; line-height: 18px; color: var(--brand-red); text-align: center; letter-spacing: 0.5px;
  }
  .card--simon .wordmark { left: 424px; }
  .card--martin .wordmark { left: 10px; }
</style>
</head>
<body>
<div class="canvas">
  <div class="board"></div>

  <section class="card card--simon">
    <svg class="rules" width="524" height="746" viewBox="0 0 524 746" aria-hidden="true">
      <path d="M511 142.5 H405.5 V736.5 H511" fill="none" stroke="var(--rule-red)" stroke-width="1.3"/>
      <line x1="299" y1="440" x2="405.5" y2="440" stroke="var(--rule-red)" stroke-width="1.3"/>
    </svg>
    <div class="wordmark">COPPERFIELD REED</div>
    <div class="details">
      <ul class="services">
        <li>PROFESSIONAL PHOTOGRAPHY</li>
        <li>WEB SOLUTIONS &amp; E-COMMERCE</li>
        <li>AUDIO &amp; HD VIDEO PRODUCTION</li>
        <li>MARKETING &amp; PROMOTIONS</li>
        <li>DESIGN, CREATION AND INSPIRATION</li>
      </ul>
      <p class="phone">T. 01632 418 720</p>
      <p class="email">SIMON@COPPERFIELDREED.EXAMPLE</p>
      <p class="person"><span class="name">SIMON <em>LATCHFORD</em></span><br><span class="role">WEB DEVELOPER</span></p>
      <p class="reg">CO #. 09264183</p>
      <address class="address">SUITE 20938, 3RD FLOOR<br>212-224 MARLOWE ROW<span class="city">LONDON,<br>EC2R 8KT</span></address>
      <p class="web">WWW.COPPERFIELDREED.EXAMPLE</p>
    </div>
  </section>

  <section class="card card--martin">
    <svg class="rules" width="524" height="746" viewBox="0 0 524 746" aria-hidden="true">
      <path d="M13 142.5 H118.5 V736.5 H13" fill="none" stroke="var(--rule-red)" stroke-width="1.3"/>
      <line x1="118.5" y1="440" x2="225" y2="440" stroke="var(--rule-red)" stroke-width="1.3"/>
    </svg>
    <div class="wordmark">COPPERFIELD REED</div>
    <div class="details">
      <ul class="services">
        <li>PROFESSIONAL PHOTOGRAPHY</li>
        <li>WEB SOLUTIONS &amp; E-COMMERCE</li>
        <li>AUDIO &amp; HD VIDEO PRODUCTION</li>
        <li>MARKETING &amp; PROMOTIONS</li>
        <li>DESIGN, CREATION AND INSPIRATION</li>
      </ul>
      <p class="phone">T. 01632 418 720</p>
      <p class="email">MARTIN@COPPERFIELDREED.EXAMPLE</p>
      <p class="person"><span class="name">MARTIN <em>OAKLEY</em></span><br><span class="role">PHOTOGRAPHER</span></p>
      <p class="reg">CO #. 09264183</p>
      <address class="address">SUITE 20938, 3RD FLOOR<br>212-224 MARLOWE ROW<span class="city">LONDON,<br>EC2R 8KT</span></address>
      <p class="web">WWW.COPPERFIELDREED.EXAMPLE</p>
    </div>
  </section>
</div>
</body>
</html>
```